Postcard About Outsourcing Paperwork

Pemberton, Inc. help nonprofits register so that they can solicit contributions in various states so essentially we are a consulting company who handles paperwork for charities. I have uploaded our logo and a couple other images that we have on our website. We want an oversized post card which on the front says something like "Tired of signing your state registrations". On the back of the card, the right half the card will need name for addresses to print. the right will have spiel about us, but could also have images. The verbiage will be something like "Not only can we file your state registrations, but we can sign and notarize them, and can cut the checks for the state fees. Pemberton file tens of thousands of state registrations each year. Call us today at 760-555-0147 or email us at info@pembertoninc.example to see how we can help you. You can also visit our website at www.pembertoninc.example"

Target Market(s)

We are targeting Charities

Industry/Entity Type

It Company

Requirements
Nice to have
• Our logo(uploaded) and the color blue (matching our logo, website, letterhead) could be good to have

```html
<!DOCTYPE html>
<html lang="en">
<head>
<meta charset="utf-8">
<title>Pemberton, Inc. Postcard</title>
<link href="https://fonts.googleapis.com/css2?family=Cinzel:wght@700;900&family=Roboto+Condensed:wght@400;700&family=Questrial&display=swap" rel="stylesheet">
<style>
:root{
  --blue:#0d4f9e;
  --tan:#b3a785;
  --beige:#ddd6c2;
  --ink:#111;
  --text:#222;
  --paper:#fff;
  --stage:#3b3b3b;
}
*{box-sizing:border-box;margin:0;padding:0}
html,body{width:900px;height:1200px;overflow:hidden;background:var(--stage)}
body{position:relative;font-family:'Questrial',sans-serif;color:var(--text)}
.card{position:absolute;left:62px;width:776px;height:502px;background:var(--paper);overflow:hidden}
.card--front{top:53px;background:linear-gradient(180deg,#f4f4f4,#ebebeb)}
.card--back{top:648px}
.abs{position:absolute}

/* front */
.brand{position:absolute;display:flex;align-items:center;gap:8px;font-family:'Roboto Condensed',sans-serif;font-weight:700;color:var(--blue)}
.brand__mark{width:44px;height:44px;background:var(--blue)}
.front__header{position:absolute;left:0;top:0;width:776px;height:112px;background:var(--paper)}
.front .brand{left:55px;top:34px;font-size:22px}
.banner{position:absolute;left:323px;top:17px;width:453px;height:95px;background:var(--blue);color:#fff;text-align:center;padding-top:10px}
.banner__q{font-size:21px;line-height:26px}
.banner__cta{font-family:'Roboto Condensed',sans-serif;font-weight:700;font-size:16px;margin-top:4px;text-transform:uppercase}
.headline{position:absolute;left:42px;top:146px;width:325px;font-family:'Cinzel',serif;font-weight:700;color:var(--ink);line-height:1;white-space:nowrap}
.headline__line{display:block;font-size:35px}
.headline__line--lg{font-size:37px}
.headline__big{display:block;font-size:47px;color:var(--blue);font-weight:900;margin:6px 0 4px}
.reasons{position:absolute;left:41px;top:318px;width:333px}
.reasons__title{font-family:'Roboto Condensed',sans-serif;font-size:25px;color:var(--blue);margin-bottom:6px}
.reasons__body{font-size:12.6px;line-height:16.5px;text-align:justify}
.web{position:absolute;left:412px;top:466px;font-size:15px;display:flex;align-items:center;gap:6px}

/* back */
.services__title{position:absolute;left:34px;top:64px;font-family:'Cinzel',serif;font-weight:700;font-size:25px;color:var(--ink)}
.services__body{position:absolute;left:34px;top:128px;width:310px;font-size:14.6px;line-height:18px}
.services__for{position:absolute;left:34px;top:254px;font-family:'Cinzel',serif;font-weight:700;font-size:18px;color:var(--blue)}
.services__list{position:absolute;left:34px;top:284px;list-style:none;font-size:18px;line-height:25px}
.services__list li{display:flex;align-items:center;gap:8px}
.contact{position:absolute;left:0;top:352px;width:440px;height:128px;padding:12px 0 0 27px}
.contact__name{font-family:'Roboto Condensed',sans-serif;font-size:21px;color:var(--blue)}
.contact__grid{display:grid;grid-template-columns:162px 220px;font-size:14px;line-height:17px;margin-top:6px}
.contact__office{font-weight:700;color:var(--ink)}
.pin{display:inline-block;vertical-align:-2px;margin-right:2px}
.contact__row{display:flex;align-items:center;gap:4px;font-size:16px;margin-top:8px}
.contact__email{font-size:14px}
.back .brand{left:507px;top:56px;font-size:14px}
.back .brand__mark{width:30px;height:30px}
.stamp{position:absolute;left:667px;top:35px;width:74px;height:87px;border:1px solid #555}
.addr-line{position:absolute;left:516px;width:226px;border-top:1px solid #999}
</style>
</head>
<body>

<section class="card card--front front">
  <div class="front__header"></div>
  <div class="brand"><span class="brand__mark"></span>Pemberton, Inc.</div>
  <div class="banner">
    <p class="banner__q">Are You Caught In The Pemberton Of<br>Complicated State Regulations?</p>
    <p class="banner__cta">Let us help you so you can focus on helping others!</p>
  </div>

  <h1 class="headline">
    <span class="headline__line">Tired of signing</span>
    <span class="headline__big">YOUR STATE</span>
    <span class="headline__line headline__line--lg">REGISTRATIONS</span>
  </h1>

  <div class="reasons">
    <h2 class="reasons__title">Reasons to Use Our Services</h2>
    <p class="reasons__body">Pemberton, Inc. has been specializing in state registrations since the 1980’s and we do more charitable state registrations than anyone (nearly 20,000 and growing all the time). Charity and fundraiser registration is not a sideline at Pemberton – it’s all we do. We handle every aspect of the registration process and would love to talk to you about helping you get registered.</p>
  </div>

  <svg class="abs" style="left:400px;top:130px" width="350" height="345" viewBox="0 0 350 345">
    <polygon points="5,62 346,5 346,345 5,290" fill="var(--tan)"/>
    <polygon points="20,75 334,22 334,328 20,277" fill="#cfd3d8" role="img" aria-label="Photo of a man standing on a white maze above tax forms"/>
  </svg>

  <div class="web">
    <svg width="12" height="12" viewBox="0 0 12 12"><circle cx="6" cy="6" r="5" fill="none" stroke="#666"/><path d="M1 6h10M6 1v10" stroke="#666"/></svg>
    www.pembertoninc.example
  </div>
</section>

<section class="card card--back back">
  <svg class="abs" style="left:0;top:0" width="500" height="502" viewBox="0 0 500 502">
    <defs>
      <linearGradient id="panelFade" x1="0" y1="0" x2="0" y2="1">
        <stop offset="0" stop-color="#fff"/><stop offset="1" stop-color="#efefef"/>
      </linearGradient>
    </defs>
    <polygon points="0,104 412,104 372,352 0,352" fill="url(#panelFade)"/>
    <polygon points="0,0 436,0 412,104 0,104" fill="#e2e4e7" role="img" aria-label="Photo of a white three-dimensional maze"/>
    <polygon points="0,352 370,352 438,480 0,480" fill="var(--beige)"/>
  </svg>

  <svg class="abs" style="left:340px;top:0" width="160" height="502" viewBox="0 0 160 502">
    <polygon points="95,0 146,0 70,350 146,502 95,502 28,350" fill="var(--tan)"/>
    <polygon points="100,0 132,0 52,350 132,502 100,502 30,350" fill="var(--blue)"/>
    <polygon points="26,120 140,138 120,222 26,210" fill="var(--blue)"/>
    <polygon points="30,124 135,141 117,218 30,206" fill="#b8bcc2" role="img" aria-label="Photo of a clock and money"/>
    <polygon points="26,238 140,236 118,348 26,338" fill="var(--blue)"/>
    <polygon points="30,242 135,240 115,344 30,334" fill="#e3dfe6" role="img" aria-label="Map of the United States"/>
  </svg>

  <h2 class="services__title">Our Services</h2>
  <p class="services__body">Filing charitable state registrations and staying in compliance with all the state regulations can feel like navigating an endless maze. Let us guide you through the pemberton, so you can focus on your mission. We handle all aspects of the state registration process.</p>
  <h3 class="services__for">Services for:</h3>
  <ul class="services__list">
    <li><svg width="13" height="13" viewBox="0 0 13 13"><circle cx="6.5" cy="6.5" r="5.5" fill="none" stroke="var(--blue)"/><path d="M4 6.5l2 2 4-4" fill="none" stroke="var(--blue)" stroke-width="1.4"/></svg>Charities</li>
    <li><svg width="13" height="13" viewBox="0 0 13 13"><circle cx="6.5" cy="6.5" r="5.5" fill="none" stroke="var(--blue)"/><path d="M4 6.5l2 2 4-4" fill="none" stroke="var(--blue)" stroke-width="1.4"/></svg>Fundraisers</li>
  </ul>

  <div class="contact">
    <p class="contact__name">Pemberton, Inc.</p>
    <div class="contact__grid">
      <div>
        <p class="contact__office">East Coast Office</p>
        <p><svg class="pin" width="9" height="13" viewBox="0 0 9 13"><path d="M4.5 12C2 8 1 6.5 1 4.5a3.5 3.5 0 0 1 7 0C8 6.5 7 8 4.5 12z" fill="none" stroke="var(--blue)" stroke-width="1.3"/></svg>412 Harbor Pike<br>Millbrook, MD 21407</p>
        <p class="contact__row"><svg width="15" height="15" viewBox="0 0 15 15"><circle cx="7.5" cy="7.5" r="6.5" fill="none" stroke="var(--blue)"/><path d="M5 4.5l1.5 2-1 1a4 4 0 0 0 2 2l1-1 2 1.5-1 1.5c-3 0-6-3-6-6z" fill="var(--blue)"/></svg>760-555-0147</p>
      </div>
      <div>
        <p class="contact__office">West Coast Office</p>
        <p><svg class="pin" width="9" height="13" viewBox="0 0 9 13"><path d="M4.5 12C2 8 1 6.5 1 4.5a3.5 3.5 0 0 1 7 0C8 6.5 7 8 4.5 12z" fill="none" stroke="var(--blue)" stroke-width="1.3"/></svg>2290 Cedar Avenue,<br>Suite 118 Seabright, CA 92010</p>
        <p class="contact__row contact__email"><svg width="14" height="10" viewBox="0 0 14 10"><rect x=".5" y=".5" width="13" height="9" fill="none" stroke="var(--blue)"/><path d="M.5.5l6.5 5 6.5-5" fill="none" stroke="var(--blue)"/></svg>info@pembertoninc.example</p>
      </div>
    </div>
  </div>

  <div class="brand"><span class="brand__mark"></span>Pemberton, Inc.</div>
  <div class="stamp"></div>
  <div class="addr-line" style="top:284px"></div>
  <div class="addr-line" style="top:320px"></div>
  <div class="addr-line" style="top:356px"></div>
</section>

</body>
</html>
```